Construction Directory Website Flyer

We need a postcard size +/- or somewhere around that size (something standard) flyer designed for our construction directory website. Leave a spot for tagline. Call to action is 'register your company now'. I am thinking many mini pictures of different construction to show that it is for the entire construction industry. Logo and screenshot of the homepage of the website is attached. Use same theme as webpage.

Target Market(s)

Construction Industry

Industry/Entity Type

Construction

Font styles to use
Sans Serif

Requirements
Must have
• Call to action
• Colors to match logo
• Area to add description and details.
Nice to have
• Construction Images
Should not have
• No Cartoonish types of things

```html
<!DOCTYPE html>
<html lang="en">
<head>
<meta charset="utf-8">
<title>BuildLink Network Flyer</title>
<link href="https://fonts.googleapis.com/css2?family=Oswald:wght@700&family=Ubuntu:wght@500;700&family=Source+Sans+3:wght@400;600&display=swap" rel="stylesheet">
<style>
  :root {
    --orange: #e0492a;
    --ink: #3b434c;
    --frame: #4a525b;
    --paper: #ffffff;
    --mist: #e9eaec;
    --backdrop: #f1f1f1;
    --text: #1d1d1d;
  }
  * { box-sizing: border-box; margin: 0; padding: 0; }
  html, body { width: 1200px; height: 1200px; overflow: hidden; background: var(--backdrop); }
  .flyer {
    position: absolute; left: 190px; top: 18px;
    width: 820px; height: 1164px;
    background: var(--paper);
    box-shadow: 0 4px 18px rgba(0,0,0,.18);
    overflow: hidden;
  }
  .block { position: absolute; }
  .header {
    left: 0; top: 0; width: 820px; height: 790px;
    background: linear-gradient(180deg, #f7f7f8 0%, #e4e5e7 22%, #f4f4f5 60%, #e7e8ea 100%);
  }
  .bar-orange { background: var(--orange); }
  .bar-frame { background: var(--frame); }
  .top-rule { left: 0; top: 0; width: 820px; height: 12px; }

  .brand {
    left: 44px; top: 70px; display: flex; align-items: center; gap: 16px;
  }
  .brand-mark { width: 54px; height: 54px; background: var(--orange); }
  .brand-name {
    font-family: "Ubuntu", sans-serif; font-weight: 500;
    font-size: 31px; line-height: 31px; color: var(--ink); letter-spacing: .5px;
  }
  .divider { left: 381px; top: 34px; width: 2px; height: 127px; background: #d4d5d8; }

  .tagline { left: 410px; top: 56px; font-family: "Ubuntu", sans-serif; font-weight: 700; }
  .tagline .line-a { display: block; color: var(--orange); font-size: 38px; line-height: 42px; }
  .tagline .line-b { display: block; color: var(--ink); font-size: 47px; line-height: 50px; }

  .photo { position: absolute; }
  .photo-paving { left: 0; top: 198px; width: 394px; height: 331px;
    background: linear-gradient(160deg, #e8742f 0%, #6a8a3d 30%, #3a3f46 55%, #2c3037 100%); }
  .photo-precast { left: 436px; top: 197px; width: 384px; height: 253px;
    background: linear-gradient(120deg, #a7a39d 0%, #8c8882 45%, #c9c4bb 75%, #b49a46 100%); }
  .photo-towers { left: 0; top: 566px; width: 392px; height: 224px;
    background: linear-gradient(180deg, #4f8fd6 0%, #8fb5de 40%, #a79a86 70%, #7f7566 100%); }
  .photo-overpass { left: 436px; top: 495px; width: 384px; height: 295px;
    background: linear-gradient(180deg, #5d9ddf 0%, #b8d4ee 40%, #b7b3ab 65%, #6f6a63 100%); }

  .register-band {
    left: 0; top: 790px; width: 820px; height: 87px;
    background: linear-gradient(180deg, #ffffff 0%, #e6e7e9 100%);
    display: flex; align-items: center; justify-content: center; gap: 22px;
  }
  .register-word { font-family: "Oswald", sans-serif; font-weight: 700; font-size: 63px; color: var(--orange); line-height: 1; }
  .register-rest { font-family: "Ubuntu", sans-serif; font-weight: 700; font-size: 36px; color: var(--ink); margin-top: 14px; }

  .about { left: 42px; top: 905px; width: 741px; }
  .about h2 { font-family: "Source Sans 3", sans-serif; font-weight: 600; font-size: 19px; color: var(--orange); line-height: 22px; }
  .about p {
    font-family: "Source Sans 3", sans-serif; font-weight: 400;
    font-size: 12.6px; line-height: 16.5px; color: var(--text);
    text-align: justify; margin-top: 2px;
  }

  .footer { left: 0; top: 1088px; width: 820px; height: 76px; background: var(--orange); }
  .phone { position: absolute; left: 46px; top: 20px; display: flex; align-items: center; gap: 10px;
    font-family: "Ubuntu", sans-serif; font-weight: 700; font-size: 27px; color: var(--text); }
  .contacts { position: absolute; left: 458px; top: 8px; font-family: "Source Sans 3", sans-serif; font-size: 19px; color: var(--text); }
  .contacts li { list-style: none; display: flex; align-items: center; gap: 12px; height: 28px; }
</style>
</head>
<body>
<main class="flyer">
  <div class="block header"></div>
  <div class="block bar-orange top-rule"></div>

  <div class="block brand">
    <span class="brand-mark"></span>
    <span class="brand-name">BuildLink<br>Network</span>
  </div>
  <div class="block divider"></div>
  <h1 class="block tagline">
    <span class="line-a">Built by Construction</span>
    <span class="line-b">for Construction</span>
  </h1>

  <div class="block bar-orange" style="left:0;top:164px;width:314px;height:17px;"></div>
  <div class="block bar-frame" style="left:410px;top:168px;width:410px;height:12px;"></div>
  <div class="block bar-frame" style="left:410px;top:168px;width:11px;height:187px;"></div>
  <div class="block bar-orange" style="left:416px;top:462px;width:404px;height:16px;"></div>
  <div class="block bar-frame" style="left:62px;top:538px;width:356px;height:16px;"></div>
  <div class="block bar-frame" style="left:403px;top:538px;width:15px;height:252px;"></div>

  <div class="photo photo-paving" role="img" aria-label="Road workers in hi-vis gear spreading fresh asphalt"></div>
  <div class="photo photo-precast" role="img" aria-label="Precast concrete forms with steel rebar and workers on site"></div>
  <div class="photo photo-towers" role="img" aria-label="High-rise residential towers under construction with cranes"></div>
  <div class="photo photo-overpass" role="img" aria-label="Concrete highway overpass under construction against blue sky"></div>

  <div class="block register-band">
    <span class="register-word">Register</span>
    <span class="register-rest">your company now</span>
  </div>
  <div class="block bar-orange" style="left:0;top:877px;width:820px;height:14px;"></div>

  <section class="block about">
    <h2>ABOUT US</h2>
    <p>Lorem Ipsum is simply dummy text of the printing and typesetting industry.Lorem Ipsum has been the industry’s standard dummy text ever since the 1500s,when an unknown printer took a galley of type and scrambled it to make a type specimen book.Lorem Ipsum is simply dummy text of the printing and typesetting industry.Lorem Ipsum has been the industry’s standard dummy text ever since the 1500s,when an unknown printer took a galley of type and scrambled it to make a type specimen book.Lorem Ipsum is simply dummy text of the printing and typesetting industry.Lorem Ipsum has been the industry’s standard dummy text ever since the 1500s,when an unknown printer took a galley of type and scrambled it to make a type specimen book.Lorem Ipsum is simply dummy text of the printing and typesetting industry.Lorem Ipsum has been the industry’s standard dummy text ever since the 1500s,when an unknown printer took a galley of type and scrambled it to make a type specimen book.</p>
  </section>

  <footer class="block footer">
    <div class="phone">
      <svg width="34" height="34" viewBox="0 0 24 24" aria-hidden="true"><path fill="#fff" d="M6.6 10.8a15.1 15.1 0 0 0 6.6 6.6l2.2-2.2c.3-.3.7-.4 1-.2 1.1.4 2.3.6 3.6.6.6 0 1 .4 1 1V20c0 .6-.4 1-1 1C10.6 21 3 13.4 3 4c0-.6.4-1 1-1h3.5c.6 0 1 .4 1 1 0 1.3.2 2.5.6 3.6.1.3 0 .7-.2 1z"/></svg>
      <span>012-555-0142</span>
    </div>
    <ul class="contacts">
      <li>
        <svg width="20" height="18" viewBox="0 0 20 18" aria-hidden="true"><rect x="1" y="4" width="18" height="13" fill="none" stroke="#fff" stroke-width="1.6"/><path d="M1 4l9 7 9-7" fill="none" stroke="#fff" stroke-width="1.6"/></svg>
        <span>info@buildlinknetwork.com</span>
      </li>
      <li>
        <svg width="20" height="18" viewBox="0 0 20 18" aria-hidden="true"><rect x="1" y="2" width="18" height="11" fill="none" stroke="#fff" stroke-width="1.6"/><path d="M7 17h6M10 13v4" stroke="#fff" stroke-width="1.6"/></svg>
        <span>www.buildlinknetwork.com</span>
      </li>
    </ul>
  </footer>
</main>
</body>
</html>
```